New Business card design to reflect rebrand

I would like a business card design with a good base colour for our new logo and also a placeholder for a profile pic of the card holder. the design needs to be editable to the point that we can easily change the picture of the person and use that design for printlarkly etc. we are looking at a metalic finish business card so will need a good base colour to bring out the finish.

Target Market(s)

prospective customers

Industry/Entity Type

Business

Contact Information for Business Card

I would like one editable design that we can change the name of the card holder and profile picture. The design need to be in a format that be send to printlarkly etc.

Our address is Fenwick Lodge, Mill Lane, Ashcombe Green, KT14 3WB Tel no. 01632 960418

Requirements
Must have
• place holder for a profile pic for the card holder. in AI or preferably PSD format

```html
<!DOCTYPE html>
<html lang="en">
<head>
<meta charset="utf-8">
<title>Brindlecore Workplace Services – Business Card</title>
<link rel="stylesheet" href="https://fonts.googleapis.com/css2?family=Source+Sans+3:wght@400;600;700&display=swap">
<style>
  :root {
    --backdrop: #e7e4df;
    --navy: #3e5069;
    --navy-deep: #2f3f55;
    --orange: #e8731f;
    --slate: #4a5468;
    --ink-soft: #5d6370;
    --rule: #8a8f98;
    --card-white: #ffffff;
    --card-fade: #eeeeee;
    --portrait-light: #b9b9b9;
    --portrait-dark: #8a8a8a;
  }
  * { box-sizing: border-box; margin: 0; padding: 0; }
  html, body {
    width: 1200px; height: 843px; overflow: hidden;
    background: var(--backdrop);
    font-family: "Source Sans 3", "Helvetica Neue", Arial, sans-serif;
  }
  .sheet { position: relative; width: 1200px; height: 843px; }

  .card {
    position: absolute; top: 261px;
    width: 560px; height: 320px;
    box-shadow: 0 8px 24px rgba(0,0,0,0.18);
    overflow: hidden;
  }

  /* Shared brand lockup */
  .brand { position: absolute; display: flex; align-items: center; gap: 14px; }
  .brand-square { width: 34px; height: 34px; flex: none; background: var(--orange); }
  .brand-name {
    font-weight: 700; text-transform: uppercase;
    font-size: 30px; line-height: 0.95; letter-spacing: 1px;
  }
  .brand-name small { display: block; font-size: 15px; letter-spacing: 3px; margin-top: 4px; }

  /* Back of card */
  .card-back {
    left: 30px;
    background: linear-gradient(160deg, var(--navy) 0%, var(--navy-deep) 100%);
  }
  .card-back .brand { top: 112px; left: 0; right: 0; justify-content: center; }
  .card-back .brand-name { color: #fff; }
  .card-back .web {
    position: absolute; bottom: 34px; left: 0; right: 0;
    text-align: center; font-size: 14px; letter-spacing: 3px;
    color: rgba(255,255,255,0.8);
  }

  /* Front of card */
  .card-front {
    left: 610px;
    background: linear-gradient(180deg, var(--card-white) 0%, var(--card-fade) 100%);
  }
  .card-front .brand { top: 34px; left: 100px; }
  .card-front .brand-name { color: var(--slate); }

  .holder { position: absolute; top: 118px; left: 36px; }
  .holder-name { font-size: 21px; font-weight: 600; color: var(--slate); line-height: 1.2; }
  .holder-role { font-size: 15px; color: var(--orange); margin-top: 2px; }

  .divider {
    position: absolute; top: 182px; left: 36px; width: 318px;
    height: 1px; background: var(--rule);
  }

  .address {
    position: absolute; top: 194px; left: 36px;
    font-style: normal; font-size: 14px; line-height: 18px; color: var(--ink-soft);
  }

  .portrait {
    position: absolute; top: 96px; right: 56px;
    width: 150px; height: 150px;
    background: linear-gradient(180deg, var(--portrait-light) 0%, var(--portrait-dark) 100%);
    border-radius: 6px;
  }

  .contact {
    position: absolute; right: 56px; bottom: 30px;
    display: flex; align-items: center; gap: 8px;
    font-size: 15px; color: var(--ink-soft);
  }
  .contact svg { width: 14px; height: 14px; }
</style>
</head>
<body>
<main class="sheet">

  <section class="card card-back" aria-label="Card back">
    <div class="brand">
      <span class="brand-square"></span>
      <span class="brand-name">Brindlecore<small>Workplace Services</small></span>
    </div>
    <p class="web">www.brindlecore.co.uk</p>
  </section>

  <section class="card card-front" aria-label="Card front">
    <div class="brand">
      <span class="brand-square"></span>
      <span class="brand-name">Brindlecore<small>Workplace Services</small></span>
    </div>

    <div class="holder">
      <p class="holder-name">Daniel Marsh</p>
      <p class="holder-role">CEO/Founder</p>
    </div>

    <div class="divider"></div>

    <address class="address">
      Fenwick Lodge<br>
      Mill Lane, Ashcombe Green<br>
      KT14 3WB
    </address>

    <div class="portrait" role="img" aria-label="Profile photo placeholder of the card holder"></div>

    <p class="contact">
      <svg viewBox="0 0 24 24" aria-hidden="true">
        <path fill="var(--orange)" d="M6.6 10.8a15.1 15.1 0 0 0 6.6 6.6l2.2-2.2a1 1 0 0 1 1-.25 11.4 11.4 0 0 0 3.6.57 1 1 0 0 1 1 1V20a1 1 0 0 1-1 1A17 17 0 0 1 3 4a1 1 0 0 1 1-1h3.5a1 1 0 0 1 1 1c0 1.25.2 2.45.57 3.57a1 1 0 0 1-.25 1z"/>
      </svg>
      01632 960418
    </p>
  </section>

</main>
</body>
</html>
```